Kestrel Hall Web Design Layout (no HTML)

We require the layout only for a website.  No html or logo is required - just the layout.

A refreshed and revitalized website to coincide with the relaunch of our brand. We are looking for a clean simplistic design that is easy to use and presents relevant information effectively.
We are an events management company specializing in conferences.
Updates

Thank you for your design. We really like the imagery. Essentially we are after a home page design (one page) that incorporates the 3 main buttons (request a proposal, select a venue and specials) while providing the relevant information on our service via functionality similar to that on www.quilbarweb.com ie using the large arrow to scroll over the relevant topic to receive information. We hope to finalise the contest in the next week and hope to consider your revised entry.

Thanks!

Target Market(s)

Australian corporate sector primarily Managing Directors or their assistants. Any business looking to hold a conference for up 500 delegates however we are primarily targeting the decision maker so need to ensure we are communicating on their terms.

Industry/Entity Type

Event

Requirements
Must have
• Incorporate the elements from the attached document however with complete creative license as to their layout. Our main competitors are plovora.com.au, harbourvexaline.com.au both sites are bland and not user friendly.
Nice to have
• Colours red, silver and black. Note we are running a separate contest to refresh our logo.
• We like the functionality of quilbarweb.com

```html
<!DOCTYPE html>
<html lang="en">
<head>
<meta charset="utf-8">
<title>Kestrel Hall – Conference Solutions</title>
<link href="https://fonts.googleapis.com/css2?family=Questrial&family=Mulish:wght@400;700;800&display=swap" rel="stylesheet">
<style>
:root{
  --red:#c1121c;
  --red-dark:#7c0f15;
  --red-light:#e0303a;
  --black:#0a0a0a;
  --grey-page:#c4c4c4;
  --grey-band:#e2e2e2;
  --grey-panel:#e6e6e6;
  --grey-header:#e8e8e8;
  --text:#111;
  --text-soft:#666;
  --white:#fff;
}
*{margin:0;padding:0;box-sizing:border-box}
html,body{width:1200px;height:721px;overflow:hidden}
body{
  position:relative;
  font-family:"Questrial",sans-serif;
  color:var(--text);
  background:linear-gradient(to bottom,#050505 0,#3a3a3a 60px,#8a8a8a 98px,var(--grey-band) 98px,var(--grey-band) 138px,var(--grey-page) 138px);
}
.page{
  position:absolute;left:159px;top:10px;width:879px;height:620px;
  background:var(--white);border-radius:8px;
  box-shadow:0 2px 10px rgba(0,0,0,.35);
}
.abs{position:absolute}
.site-header{left:8px;top:7px;width:863px;height:69px;background:var(--grey-header);border-radius:4px}
.brand{left:40px;top:10px;font-size:38px;color:#555;letter-spacing:-.5px}
.search-label{left:574px;top:53px;font-family:"Mulish",sans-serif;font-weight:800;font-size:13px}
.search-input{left:637px;top:52px;width:175px;height:18px;background:var(--white);border:1px solid #ddd}
.search-go{left:814px;top:48px;width:28px;height:28px;border-radius:4px;
  background:linear-gradient(#e8414a,#a80f18);border:1px solid #8a0c12;
  color:var(--white);font-family:"Mulish",sans-serif;font-weight:800;font-size:11px;
  display:flex;align-items:center;justify-content:center}
.header-rule{left:8px;top:77px;width:863px;height:8px;
  background:linear-gradient(to right,#fff 0,#bbb 25%,#222 50%,#bbb 75%,#fff 100%)}
.nav{left:0;top:113px;width:150px}
.nav a{position:absolute;left:21px;font-size:14px;color:var(--text);text-decoration:none;white-space:nowrap}
.nav .active-tab{position:absolute;left:5px;top:0;width:136px;height:30px}
.nav a.active{color:var(--white);top:7px}
.intro{left:168px;top:104px;width:610px;font-size:16px;line-height:20px}
.intro b{font-family:"Mulish",sans-serif;font-weight:800}
.packages{left:149px;top:180px;width:493px;height:283px;background:var(--grey-panel);border-radius:8px}
.packages h2{position:absolute;left:33px;top:24px;font-family:"Mulish",sans-serif;font-weight:700;font-size:15px;color:var(--text-soft)}
.dollar-art{left:29px;top:70px;width:80px;height:151px;border-radius:40px 40px 30px 30px;
  background:linear-gradient(160deg,#f0444c,#b30d15 60%,#7a0a0f)}
.package-list{position:absolute;left:148px;top:60px;list-style:none;font-size:12.5px;line-height:15.7px;color:var(--text-soft)}
.package-list li::before{content:"•";margin-right:8px}
.package-note{position:absolute;left:148px;top:196px;width:345px;font-size:12.5px;line-height:15.5px;color:var(--text-soft)}
.goals{left:650px;top:180px;width:202px;height:287px;border-radius:8px;
  background:linear-gradient(to bottom,var(--red) 0,#a5141c 55%,var(--red-dark) 100%)}
.goals h3{position:absolute;left:6px;top:15px;width:196px;font-family:"Mulish",sans-serif;font-weight:800;font-size:15px;line-height:19px;color:var(--white)}
.goal-pointer{left:596px;top:250px;width:252px;height:60px}
.goal{position:absolute;left:661px;font-size:20px;line-height:22px;color:var(--white);white-space:nowrap}
.goal.current{left:661px;top:285px}
.feature{position:absolute;top:479px;width:199px}
.feature .tab{height:18px;background:var(--red);border-radius:0 4px 0 0;color:var(--white);font-size:12px;line-height:18px;padding-left:8px}
.feature p{position:absolute;left:3px;top:25px;width:115px;font-family:"Mulish",sans-serif;font-size:11px;line-height:13px}
.feature .art{position:absolute;top:23px;width:70px;height:70px}
.offers{left:150px}
.proposal{left:397px}
.browse{left:652px}
.divider{position:absolute;top:505px;width:1px;height:112px;background:linear-gradient(#fff,#ccc 30%,#ccc 70%,#fff)}
.site-footer{left:8px;top:588px;width:863px;height:24px;background:var(--black);border-radius:3px;
  color:var(--white);font-family:"Mulish",sans-serif;font-size:10px;line-height:24px;text-align:center}
</style>
</head>
<body>
<div class="page">
  <header class="abs site-header"></header>
  <div class="abs brand">kestrel hall</div>
  <div class="abs search-label">SEARCH:</div>
  <div class="abs search-input"></div>
  <div class="abs search-go">GO</div>
  <div class="abs header-rule"></div>

  <nav class="abs nav">
    <svg class="active-tab" viewBox="0 0 136 30" aria-hidden="true">
      <defs><linearGradient id="tabFill" x1="0" y1="0" x2="0" y2="1">
        <stop offset="0" stop-color="#e23a44"/><stop offset="1" stop-color="#a30d16"/></linearGradient></defs>
      <path d="M0 2 Q0 0 2 0 H118 L136 15 L118 30 H2 Q0 30 0 28 Z" fill="url(#tabFill)"/>
    </svg>
    <a class="active" href="#">HOME</a>
    <a href="#" style="top:35px">SERVICES</a>
    <a href="#" style="top:63px">VENUES</a>
    <a href="#" style="top:91px">CLIENTS</a>
    <a href="#" style="top:119px">REGISTER</a>
    <a href="#" style="top:146px">CONTACT US</a>
  </nav>

  <p class="abs intro"><b>Kestrel Hall</b>’ professional conference team specialises in solutions. We work closely with a core group of clients to ensure desired outcomes, on time and in budget.</p>

  <section class="abs packages">
    <h2>We offer a complete range of finance&nbsp; packages including;</h2>
    <div class="abs dollar-art" role="img" aria-label="Large red 3D dollar sign illustration"></div>
    <ul class="package-list">
      <li>total conference underwriting</li>
      <li>online delegate payment gateway</li>
      <li>substantially discounted rooming rates</li>
      <li>no upfront costs</li>
      <li>zero management fees</li>
      <li>free venue sourcing</li>
      <li>free delegate booking management</li>
    </ul>
    <p class="package-note">Minimise your costs and free your cash flow to focus on your core business functions. We’ll ensure maximum return from your conference budget.</p>
  </section>

  <section class="abs goals">
    <h3>Our goal is to make sure your conference is:</h3>
  </section>
  <svg class="abs goal-pointer" viewBox="0 0 252 60" aria-hidden="true">
    <defs><linearGradient id="pointerFill" x1="0" y1="0" x2="0" y2="1">
      <stop offset="0" stop-color="#555"/><stop offset="1" stop-color="#151515"/></linearGradient></defs>
    <path d="M2 30 L24 2 H246 Q250 2 250 6 V54 Q250 58 246 58 H24 Z" fill="url(#pointerFill)" stroke="#fff" stroke-width="3"/>
  </svg>
  <div class="goal current">Cost Effective</div>
  <div class="goal" style="top:331px">Expertely Managed<br>&amp; Hassle Free</div>
  <div class="goal" style="top:390px">Outcome Focussed</div>
  <div class="goal" style="top:433px">Well Attended</div>

  <section class="feature offers">
    <div class="tab">Special Offers</div>
    <p>Not sure where to start? We have over 60 properties to choose from both domestically and international.</p>
    <div class="art" role="img" aria-label="Red seal badge with dollar sign" style="left:128px;border-radius:50%;background:radial-gradient(circle at 40% 35%,#f25058,#b8101a 70%)"></div>
  </section>
  <div class="divider" style="left:374px"></div>
  <section class="feature proposal">
    <div class="tab">Request Proposal</div>
    <p>Not sure where to start? We have over 60 properties to choose from both domestically and international.</p>
    <div class="art" role="img" aria-label="Wall clock illustration" style="left:136px;border-radius:50%;background:radial-gradient(circle,#fafafa 55%,#ddd 62%,#b3121b 66%,#8a0c12)"></div>
  </section>
  <div class="divider" style="left:638px"></div>
  <section class="feature browse">
    <div class="tab">Browse Conference</div>
    <p>Not sure where to start? We have over 60 properties to choose from both domestically and international.</p>
    <div class="art" role="img" aria-label="Red map of Australia illustration" style="left:116px;border-radius:30% 40% 35% 45%;background:linear-gradient(150deg,#ee3b44,#a50d16)"></div>
  </section>

  <footer class="abs site-footer">Ph: 1300 555 014. P.O. Box 4471, Lindfield Bay NSW 2077. Kestrel Hall. All Rights Reserved. 2009</footer>
</div>
</body>
</html>
```